Design for Training Manuals

We need a graphic design for new training manuals for our organization called Lanternfield Trust, Inc. We are a children's rights NGO based in the Philippines. We are running an advocacy campaign called Raise Every Voice which advocates for the prevention of child sexual abuse and sexual exploitation of children. The Raise Every Voice Campaign is gaining momentum in various countries around the world and we would like to provide our constituents with inspiring training materials that will enable them to carry out the work of protecting children's rights.
Because of the sensitive nature of the subject matter, we would like to present a non-threatening light design, with a creative edge, that incorporates our Raise Every Voice logo. Also, I have attached an image from which you can design from.
Please feel free to visit our website for inspiration: www.lanternfieldtrust.org
Updates
Dear Designers,
I am excited about this project. I have uploaded a couple of our training modules. Overall there are 2 levels: Level 1 with 3 training modules and Level 2 also with 3 training modules.
Thank you,
Delia
Target Market(s)
Non-government workers, government workers, teachers, social workers...
Industry/Entity Type
Graphic Design
Look and feel
Each slider illustrates characteristics of the customer's brand and the style your logo design should communicate.

```html
<!DOCTYPE html>
<html lang="en">
<head>
<meta charset="utf-8">
<title>Raise Every Voice – Level Three Training Manual</title>
<link rel="stylesheet" href="https://fonts.googleapis.com/css2?family=EB+Garamond:wght@600;700;800&family=Arimo:wght@400;700&display=swap">
<style>
  :root {
    --teal-dark: #6a9593;
    --sage-light: #abc2b3;
    --paper: #ffffff;
    --ink: #2b2b2b;
    --ink-soft: #6b6b6b;
    --frame: #9a9a9a;
    --level-teal: #5f8f8c;
    --level-sage: #a4bcae;
    --badge: #f08a24;
  }
  html, body {
    margin: 0;
    padding: 0;
    width: 928px;
    height: 1200px;
    overflow: hidden;
    background: var(--paper);
  }
  .manual-cover {
    display: block;
    width: 928px;
    height: 1200px;
  }
  .serif { font-family: "EB Garamond", Georgia, serif; }
  .sans { font-family: "Arimo", Arial, sans-serif; }
  .shape-dark { fill: var(--teal-dark); }
  .shape-light { fill: var(--sage-light); }
  .cover-frame { fill: none; stroke: var(--frame); stroke-width: 2; }
  .level-word { fill: var(--level-teal); font-weight: 700; font-size: 44px; }
  .level-number { fill: var(--level-sage); font-weight: 600; font-size: 62px; }
  .module-title { fill: var(--ink); font-size: 21px; }
  .campaign-title { fill: var(--paper); font-weight: 700; }
  .campaign-small { font-size: 104px; }
  .campaign-large { font-size: 214px; font-weight: 800; }
  .tagline { fill: var(--ink); font-size: 25px; }
  .footer-org { fill: var(--ink-soft); font-size: 16px; letter-spacing: 0.3px; }
  .footer-url { fill: var(--ink-soft); font-size: 16px; }
  .brand-rule { stroke: var(--ink); stroke-width: 1.2; }
  .brand-dot { fill: var(--badge); }
  .brand-name { fill: var(--ink); font-size: 12px; font-weight: 700; }
</style>
</head>
<body>
<svg class="manual-cover" viewBox="0 0 928 1200" xmlns="http://www.w3.org/2000/svg" aria-label="Raise Every Voice training manual cover, level three">
  <g class="geometric-backdrop" transform="scale(1.25)">
    <polygon class="shape-dark" points="0,0 237,0 237,775 0,540"/>
    <polygon class="shape-light" points="237,420 325,333 500,510 500,775 237,775"/>
    <polygon class="shape-dark" points="237,640 500,510 500,775 237,775"/>
    <polygon class="shape-light" points="500,510 676,333 742,333 742,640 600,775 500,775"/>
    <polygon class="shape-dark" points="676,333 742,333 742,640 600,775 530,775"/>
    <polygon class="shape-light" points="610,775 742,640 742,910"/>
  </g>

  <rect class="cover-frame" x="1" y="1" width="926" height="1198"/>

  <g class="brand-mark">
    <line class="brand-rule" x1="679" y1="25" x2="904" y2="25"/>
    <circle class="brand-dot" cx="810" cy="84" r="28"/>
    <text class="brand-name sans" x="810" y="136" text-anchor="middle">LANTERNFIELD TRUST INC.</text>
  </g>

  <g class="level-label">
    <text x="348" y="292"><tspan class="level-word serif">level</tspan><tspan class="level-number serif" dx="4">three</tspan></text>
    <text class="module-title sans" x="350" y="325">Module I: Module Title</text>
  </g>

  <g class="campaign-lockup">
    <text class="campaign-title campaign-small serif" x="94" y="656">raise</text>
    <text class="campaign-title campaign-small serif" x="206" y="765">every</text>
    <text class="campaign-title campaign-large serif" x="222" y="962">Voice</text>
    <text class="tagline sans" x="272" y="1004">Stop child sexual abuse and exploitation</text>
  </g>

  <g class="cover-footer">
    <text class="footer-org sans" x="29" y="1133">LANTERNFIELD TRUST INC.</text>
    <text class="footer-url sans" x="56" y="1155">www.lanternfieldtrust.org</text>
  </g>
</svg>
</body>
</html>
```